Halden & Pruitt Periodontics and Implant Solutions Business Card

We are a specialty dental practice- implants and periodontal surgery. We have just re-designed our logo and are building a new office and would like to re-design our business card. We are looking for something professional with a creative and artsy twist- something to stand out among the rest! Happy Designing!

I have uploaded all versions of our new logo and our current business card. We have 3 locations and 2 doctors.

Target Market(s)

55+

Industry/Entity Type

Dental

Contact Information for Business Card

Needs Names, logo, locations- professional and artsy!

Colors
0555a3
0592cd
34a7d7
3277b5
85cae6
85acd3
cee9f5
ecf7fb

Requirements
Must have
• our names:
• Thomas E. Halden D.M.D.
• Celia M. Pruitt D.M.D.
• Diplomate of the National Council of Gum Surgery
• Address locations:
• 462 W. Larkspur Avenue Suite 210B Plantation, FL 33871
• Tel: 954-318-2264 Fax: 954-318-2291
• 5127 Harlow Lane #C-4 Boca Raton, FL 33609
• Tel: 561-627-1958 Fax: 561-703-2816
• 274 Northwest 9th Street #412 Miami FL 33987
• Tel: 786-429-6153 Fax: 786-429-6170
Nice to have
• unique look
Should not have
• doesn't need QR like our current card has.

```html
<!DOCTYPE html>
<html lang="en">
<head>
<meta charset="utf-8">
<title>Halden &amp; Pruitt Business Card</title>
<link rel="stylesheet" href="https://fonts.googleapis.com/css2?family=Questrial&display=swap">
<style>
  :root {
    --navy: #2a4888;
    --navy-deep: #223c76;
    --navy-light: #3c5ea3;
    --ink: #2f4d8c;
    --grey: #8a8a8a;
    --grey-light: #b9b9b9;
    --paper: #ffffff;
    --stage: #e9ebee;
    --white: #ffffff;
  }
  * { margin: 0; padding: 0; box-sizing: border-box; }
  html, body {
    width: 1200px; height: 843px; overflow: hidden;
    background: var(--stage);
    font-family: "Questrial", sans-serif;
  }
  .canvas {
    width: 1200px; height: 843px;
    display: flex; align-items: center; justify-content: center; gap: 40px;
  }
  .card {
    width: 540px; height: 309px;
    background: var(--paper);
    box-shadow: 0 6px 18px rgba(0,0,0,0.12);
    position: relative; overflow: hidden;
  }
  /* Front */
  .card-front { display: flex; align-items: center; justify-content: center; }
  .brand { display: flex; align-items: center; gap: 16px; color: var(--ink); }
  .brand-dot {
    width: 74px; height: 74px; border-radius: 50%;
    border: 5px solid var(--navy);
  }
  .brand-name { font-size: 33px; letter-spacing: 0.5px; line-height: 1.05; }
  .brand-tagline { font-size: 15px; letter-spacing: 0.2px; }
  /* Back */
  .card-back { display: flex; }
  .locations {
    width: 262px; height: 100%;
    background: linear-gradient(135deg, var(--navy-deep) 0%, var(--navy) 55%, var(--navy-light) 100%);
    color: var(--white);
    padding: 20px 18px 18px 22px;
    display: flex; flex-direction: column; justify-content: space-between;
    font-size: 12.5px; line-height: 1.32;
  }
  .location + .location {
    border-top: 1.5px dotted rgba(255,255,255,0.8);
    padding-top: 8px;
  }
  .location { padding-bottom: 4px; }
  .line-phone { display: flex; align-items: center; gap: 6px; }
  .line-phone svg { width: 11px; height: 11px; fill: var(--white); flex: none; }
  .details {
    flex: 1; padding: 60px 22px 20px 26px;
    display: flex; flex-direction: column;
  }
  .details .brand-name { font-size: 22px; color: var(--ink); }
  .details .brand-tagline { font-size: 10.5px; color: var(--ink); margin-bottom: 26px; }
  .doctor { font-size: 15.5px; color: var(--ink); line-height: 1.35; }
  .credential { font-size: 12.5px; color: var(--grey); line-height: 1.3; margin-top: 8px; }
  .email { font-size: 13px; color: var(--grey); margin-top: 6px; }
</style>
</head>
<body>
<main class="canvas">
  <section class="card card-front" aria-label="Card front">
    <div class="brand">
      <span class="brand-dot"></span>
      <div>
        <div class="brand-name">HALDEN &amp; PRUITT</div>
        <div class="brand-tagline">Periodontics and Implant Solutions</div>
      </div>
    </div>
  </section>

  <section class="card card-back" aria-label="Card back">
    <div class="locations">
      <div class="location">
        <div>462 W. Larkspur Avenue</div>
        <div>Suite 210B, Plantation, FL 33871</div>
        <div class="line-phone"><svg viewBox="0 0 24 24"><path d="M6.6 10.8a15.1 15.1 0 0 0 6.6 6.6l2.2-2.2c.3-.3.7-.4 1-.2 1.1.4 2.3.6 3.6.6.6 0 1 .4 1 1V20c0 .6-.4 1-1 1A17 17 0 0 1 3 4c0-.6.4-1 1-1h3.5c.6 0 1 .4 1 1 0 1.3.2 2.5.6 3.6.1.3 0 .7-.2 1z"/></svg>954-318-2264</div>
        <div class="line-phone"><svg viewBox="0 0 24 24"><path d="M6 2h12v5H6zM3 8h18a1 1 0 0 1 1 1v8h-4v5H6v-5H2V9a1 1 0 0 1 1-1zm5 8v4h8v-4z"/></svg>954-318-2291</div>
      </div>
      <div class="location">
        <div>5127 Harlow Lane</div>
        <div>#C-4 Boca Raton, FL 33609</div>
        <div class="line-phone"><svg viewBox="0 0 24 24"><path d="M6.6 10.8a15.1 15.1 0 0 0 6.6 6.6l2.2-2.2c.3-.3.7-.4 1-.2 1.1.4 2.3.6 3.6.6.6 0 1 .4 1 1V20c0 .6-.4 1-1 1A17 17 0 0 1 3 4c0-.6.4-1 1-1h3.5c.6 0 1 .4 1 1 0 1.3.2 2.5.6 3.6.1.3 0 .7-.2 1z"/></svg>561-627-1958</div>
        <div class="line-phone"><svg viewBox="0 0 24 24"><path d="M6 2h12v5H6zM3 8h18a1 1 0 0 1 1 1v8h-4v5H6v-5H2V9a1 1 0 0 1 1-1zm5 8v4h8v-4z"/></svg>561-703-2816</div>
      </div>
      <div class="location">
        <div>274 Northwest</div>
        <div>9th Street #412, Miami FL 33987</div>
        <div class="line-phone"><svg viewBox="0 0 24 24"><path d="M6.6 10.8a15.1 15.1 0 0 0 6.6 6.6l2.2-2.2c.3-.3.7-.4 1-.2 1.1.4 2.3.6 3.6.6.6 0 1 .4 1 1V20c0 .6-.4 1-1 1A17 17 0 0 1 3 4c0-.6.4-1 1-1h3.5c.6 0 1 .4 1 1 0 1.3.2 2.5.6 3.6.1.3 0 .7-.2 1z"/></svg>786-429-6153</div>
        <div class="line-phone"><svg viewBox="0 0 24 24"><path d="M6 2h12v5H6zM3 8h18a1 1 0 0 1 1 1v8h-4v5H6v-5H2V9a1 1 0 0 1 1-1zm5 8v4h8v-4z"/></svg>786-429-6170</div>
      </div>
    </div>
    <div class="details">
      <div class="brand-name">HALDEN &amp; PRUITT</div>
      <div class="brand-tagline">Periodontics and Implant Solutions</div>
      <div class="doctor">Thomas E. Halden D.M.D.</div>
      <div class="doctor">Celia M. Pruitt D.M.D.</div>
      <div class="credential">Diplomate of the National<br>Council of Gum Surgery Founder</div>
      <div class="email">info@haldenpruitt.com</div>
    </div>
  </section>
</main>
</body>
</html>
```